Business card design needed

Just need something dynamic and unique
For a local painting contractor

Industry/Entity Type

Painting

Contact Information for Business Card

Warren Pike
Painting Contactor
Interior & Exterior
New Work & Repaints
For an obligation free quote:
0437516082

```html
<!DOCTYPE html>
<html lang="en">
<head>
<meta charset="utf-8">
<title>Warren Pike – Painting Contactor</title>
<link rel="stylesheet" href="https://fonts.googleapis.com/css2?family=Questrial&family=Arimo:wght@700&family=Mountains+of+Christmas:wght@700&display=swap">
<style>
  :root {
    --card-black: #050607;
    --card-glow: #141c26;
    --text-white: #ffffff;
    --text-soft: #f2f2f2;
    --tone-blue: #3c8fd0;
    --tone-green: #3ccf5a;
    --tone-yellow: #d9dc3e;
    --tone-cream: #efc47a;
    --tone-orange: #ef6a1e;
    --tone-red: #e0223c;
    --tone-magenta: #d22ea2;
    --tone-violet: #7a40d0;
  }
  html, body {
    margin: 0;
    padding: 0;
    width: 1200px;
    height: 703px;
    overflow: hidden;
    background: var(--card-black);
  }
  .card {
    position: relative;
    width: 1200px;
    height: 703px;
    overflow: hidden;
    background: radial-gradient(ellipse 70% 55% at 50% 45%, var(--card-glow) 0%, var(--card-black) 75%);
    color: var(--text-white);
  }
  .ribbon-art {
    position: absolute;
    left: 0;
    top: 200px;
    width: 1200px;
    height: 250px;
    background: linear-gradient(90deg,
      transparent 0%,
      var(--tone-blue) 6%,
      var(--tone-green) 18%,
      var(--tone-yellow) 34%,
      var(--tone-cream) 48%,
      var(--tone-orange) 62%,
      var(--tone-red) 76%,
      var(--tone-magenta) 88%,
      var(--tone-violet) 95%,
      transparent 100%);
    -webkit-mask-image: linear-gradient(180deg, transparent 0%, #000 35%, #000 65%, transparent 100%);
    mask-image: linear-gradient(180deg, transparent 0%, #000 35%, #000 65%, transparent 100%);
    opacity: 0.85;
  }
  .owner {
    position: absolute;
    left: 64px;
    top: 48px;
    margin: 0;
    font-weight: 400;
  }
  .owner-name {
    display: block;
    font-family: "Questrial", "Century Gothic", sans-serif;
    font-size: 56px;
    line-height: 1;
    letter-spacing: 0.5px;
  }
  .owner-role {
    display: block;
    margin-top: 14px;
    font-family: "Questrial", "Century Gothic", sans-serif;
    font-size: 31px;
    line-height: 1;
    color: var(--text-soft);
  }
  .quote {
    position: absolute;
    right: 64px;
    top: 60px;
    text-align: right;
  }
  .quote-label {
    display: block;
    font-family: "Questrial", "Century Gothic", sans-serif;
    font-size: 31px;
    line-height: 1;
    color: var(--text-soft);
  }
  .quote-phone {
    display: block;
    margin-top: 14px;
    font-family: "Arimo", Arial, sans-serif;
    font-weight: 700;
    font-size: 46px;
    line-height: 1;
    letter-spacing: 1px;
  }
  .services {
    position: absolute;
    left: 0;
    right: 0;
    top: 600px;
    margin: 0;
    text-align: center;
    font-family: "Mountains of Christmas", cursive;
    font-weight: 700;
    font-size: 46px;
    line-height: 1;
    letter-spacing: 1px;
  }
</style>
</head>
<body>
  <div class="card">
    <div class="ribbon-art" role="img" aria-label="Flowing rainbow paint ribbon artwork across the card"></div>

    <h1 class="owner">
      <span class="owner-name">Warren Pike</span>
      <span class="owner-role">Painting Contactor</span>
    </h1>

    <div class="quote">
      <span class="quote-label">For an obligation free quote</span>
      <span class="quote-phone">0437516082</span>
    </div>

    <p class="services">Interior &amp; Exterior New Work &amp; Repaints</p>
  </div>
</body>
</html>
```